Back Pain

Need a flyer similar to the attached draft. This is to be handed out to prospective patients. Note that Sketch Hive has already designed the logo. If you need a copy please contact me

```html
<!DOCTYPE html>
<html lang="en">
<head>
<meta charset="utf-8">
<title>Tech Neck – Spine Ease Clinic Flyer</title>
<link rel="stylesheet" href="https://fonts.googleapis.com/css2?family=Michroma&family=Roboto+Condensed:wght@300;400;700&family=Montserrat:wght@600&display=swap">
<style>
  :root {
    --ink: #0b0b0b;
    --green: #9cc64a;
    --blue: #4472c4;
    --teal: #5f93a8;
    --white: #ffffff;
  }
  * { margin: 0; padding: 0; box-sizing: border-box; }
  html, body { width: 985px; height: 1200px; overflow: hidden; background: var(--ink); }
  .flyer {
    position: relative; width: 985px; height: 1200px;
    background: var(--ink); color: var(--white);
    font-family: "Roboto Condensed", "Arial Narrow", sans-serif;
  }
  .runner-figure {
    position: absolute; left: 360px; top: 60px; width: 470px; height: 700px;
    border-radius: 48% 52% 40% 60% / 30% 30% 70% 70%;
    background: linear-gradient(160deg, rgba(156,198,74,.85) 0%, rgba(95,147,168,.7) 45%, rgba(68,114,196,.8) 100%);
    opacity: .55;
  }
  .headline {
    position: absolute; left: 90px; top: 110px;
    font-family: "Michroma", sans-serif; color: var(--green);
    font-size: 86px; line-height: 1.05; letter-spacing: -2px;
  }
  .headline span { display: block; }
  .headline .neck { margin-left: -10px; }
  .symptoms {
    position: absolute; right: 545px; top: 355px; list-style: none; text-align: right;
    font-family: "Michroma", sans-serif; color: var(--green);
    font-size: 26px; line-height: 50px;
  }
  .force-chart { position: absolute; left: 600px; top: 325px; width: 300px; }
  .force-chart__title {
    text-align: right; font-weight: 700; font-size: 19px; line-height: 24px; text-transform: uppercase;
  }
  .force-chart svg { display: block; margin-top: 10px; }
  .swoosh { position: absolute; left: 0; top: 0; }
  .screen-time { position: absolute; left: 520px; top: 650px; display: flex; align-items: center; gap: 18px; }
  .screen-time__text { font-size: 22px; font-weight: 300; line-height: 27px; text-transform: uppercase; }
  .screen-time__text strong { display: block; font-size: 30px; font-weight: 700; line-height: 34px; }
  .care-message {
    position: absolute; left: 80px; top: 810px; font-weight: 400; text-transform: uppercase;
    font-size: 30px; line-height: 36px;
  }
  .care-message .small { font-size: 25px; }
  .clinic-name {
    position: absolute; left: 110px; top: 970px; width: 330px; text-align: center;
    font-family: "Montserrat", sans-serif; font-weight: 600; color: var(--blue);
  }
  .clinic-name__mark {
    display: block; width: 110px; height: 110px; margin: 0 auto 18px; border-radius: 50%;
    border: 6px solid var(--teal);
  }
  .clinic-name__title { font-size: 30px; letter-spacing: -0.5px; }
  .clinic-name__sub { font-size: 13px; letter-spacing: 3px; margin-top: 2px; }
  .practice-info {
    position: absolute; right: 70px; top: 870px; text-align: right; text-transform: uppercase;
    font-size: 28px; line-height: 36px; font-weight: 300;
  }
  .practice-info strong { font-weight: 700; }
  .web-link {
    position: absolute; left: 555px; top: 1090px; width: 370px; height: 44px; border-radius: 22px 0 0 22px;
    background: linear-gradient(90deg, var(--blue), var(--green));
    font-weight: 700; font-size: 24px; line-height: 44px; text-align: center;
  }
</style>
</head>
<body>
<main class="flyer">
  <div class="runner-figure" role="img" aria-label="Stylised running figure in green-to-blue gradient with spine dots along its back"></div>

  <svg class="swoosh" width="985" height="1200" aria-hidden="true">
    <defs>
      <linearGradient id="swooshGrad" x1="0" x2="1" y1="0" y2="0">
        <stop offset="0" stop-color="#4472c4"/>
        <stop offset="1" stop-color="#9cc64a"/>
      </linearGradient>
    </defs>
    <path d="M45 770 L380 760 C470 755 470 650 560 645 L885 628" fill="none" stroke="url(#swooshGrad)" stroke-width="4"/>
  </svg>

  <h1 class="headline"><span>TECH</span><span class="neck">NECK</span></h1>

  <ul class="symptoms">
    <li>HEADACHES</li>
    <li>NECK PAIN</li>
    <li>SHOULDER PAIN</li>
    <li>ARM &amp; HAND PAIN</li>
    <li>BACK PAIN</li>
    <li>SCIATICA</li>
  </ul>

  <section class="force-chart">
    <p class="force-chart__title">As the head tilts<br>forward more force is<br>placedon the spine</p>
    <svg width="300" height="200" viewBox="0 0 300 200" role="img" aria-label="Bar chart: force on spine 12 at 0°, 27 at 15°, 40 at 30°, 49 at 45°, 60 at 60°">
      <defs>
        <linearGradient id="barGrad" x1="0" x2="0" y1="0" y2="1">
          <stop offset="0" stop-color="#9cc64a"/>
          <stop offset=".55" stop-color="#4472c4"/>
        </linearGradient>
      </defs>
      <g fill="url(#barGrad)">
        <rect x="40" y="137" width="38" height="28"/>
        <rect x="92" y="103" width="38" height="62"/>
        <rect x="144" y="73" width="38" height="92"/>
        <rect x="196" y="52" width="38" height="113"/>
        <rect x="248" y="27" width="38" height="138"/>
      </g>
      <g fill="#fff" font-family="Roboto Condensed, sans-serif" font-weight="700" font-size="20" text-anchor="middle">
        <text x="59" y="158">12</text>
        <text x="111" y="126">27</text>
        <text x="163" y="96">40</text>
        <text x="215" y="75">49</text>
        <text x="267" y="50">60</text>
      </g>
      <g fill="#fff" font-family="Roboto Condensed, sans-serif" font-weight="700" font-size="18" text-anchor="middle">
        <text x="59" y="190">0°</text>
        <text x="111" y="190">15°</text>
        <text x="163" y="190">30°</text>
        <text x="215" y="190">45°</text>
        <text x="267" y="190">60°</text>
      </g>
    </svg>
  </section>

  <section class="screen-time">
    <svg width="96" height="96" viewBox="0 0 96 96" role="img" aria-label="Pie chart showing share of the day spent on devices">
      <defs>
        <linearGradient id="pieGrad" x1="0" x2="1">
          <stop offset="0" stop-color="#4472c4"/>
          <stop offset="1" stop-color="#9cc64a"/>
        </linearGradient>
      </defs>
      <circle cx="48" cy="48" r="46" fill="#fff"/>
      <path d="M48 48 L48 2 A46 46 0 0 1 76 84 Z" fill="url(#pieGrad)"/>
      <path d="M48 48 L48 2 M48 48 L76 84" stroke="#0b0b0b" stroke-width="4"/>
    </svg>
    <p class="screen-time__text">The average person spends<strong>8-11 hours per day</strong>using electronic divices</p>
  </section>

  <p class="care-message">Chiropractic care can help<br><span class="small">correct and prevent these problems</span><br>by restoring and maintaning<br>proper alignment of the neck</p>

  <div class="clinic-name">
    <span class="clinic-name__mark"></span>
    <p class="clinic-name__title">SPINE EASE CLINIC</p>
    <p class="clinic-name__sub">DR SAM CARVER - CHIROPRACTOR</p>
  </div>

  <p class="practice-info">
    <strong>Dr. Samuel Carver</strong><br>
    Now in Portside at<br>
    72 Quay Rd - <strong>Harbour Suites</strong><br>
    <strong>50% off</strong> initial consultation<br>
    if now <strong>book online</strong> at
  </p>

  <p class="web-link">www.spineeaseclinic.com.au</p>
</main>
</body>
</html>
```